Simple and Clean business card design

We would like the design to be simple clean and to incorporate our colors.

We are open to your design and talent, we have the dots in our logo as we think of it as data points and we connect data points for people.

We are open to see the great creative and clean design you bring to the table

Contact Information for Business Card

please include: name, position, email, phone and website

Font styles to use
Sans Serif

Requirements
Must have
• my colors incorporated, simplicity
Nice to have
• lots of white space, simplicity
Should not have
• complexicity/ complex art

```html
<!DOCTYPE html>
<html lang="en">
<head>
<meta charset="utf-8">
<title>Nectra Business Card</title>
<link rel="stylesheet" href="https://fonts.googleapis.com/css2?family=Open+Sans:wght@400;600&display=swap">
<style>
  :root {
    --backdrop: #58595b;
    --card-white: #f7f8f9;
    --tint-blue: #dcecf8;
    --accent-blue: #4f78c8;
    --band-blue: #7fa3da;
    --icon-blue: #5b82cf;
    --brand-green: #35b24a;
    --ink: #2b2b2b;
    --ink-soft: #3d3d3d;
  }
  * { box-sizing: border-box; margin: 0; padding: 0; }
  html, body { width: 1200px; height: 961px; overflow: hidden; }
  body {
    background: var(--backdrop);
    font-family: "Open Sans", Arial, sans-serif;
    display: flex;
    align-items: center;
    justify-content: center;
    gap: 44px;
  }
  .card {
    position: relative;
    width: 530px;
    height: 303px;
    background: var(--card-white);
    overflow: hidden;
    box-shadow: 0 10px 28px rgba(0,0,0,.35);
  }
  .card-tint {
    position: absolute;
    inset: 0;
    background: linear-gradient(120deg, rgba(255,255,255,0) 35%, var(--tint-blue) 100%);
  }
  .wordmark {
    position: absolute;
    display: flex;
    align-items: center;
    gap: 8px;
    font-weight: 600;
    color: var(--ink);
    letter-spacing: 1px;
  }
  .wordmark-dot {
    width: 10px; height: 10px;
    border-radius: 50%;
    background: var(--brand-green);
  }
  .rule {
    position: absolute;
    height: 1.5px;
    background: var(--accent-blue);
  }

  /* Front */
  .front .wordmark { top: 34px; right: 40px; font-size: 40px; }
  .front .rule { left: 150px; right: 0; top: 150px; }
  .holder { position: absolute; left: 34px; top: 120px; }
  .holder-name { font-size: 22px; color: var(--ink); line-height: 1.1; }
  .holder-name .first { color: var(--brand-green); }
  .holder-role { font-size: 16px; color: var(--ink-soft); margin-top: 2px; }
  .contact {
    position: absolute;
    font-size: 12.5px;
    color: var(--ink-soft);
    line-height: 1.6;
  }
  .contact-icon {
    display: block;
    width: 20px; height: 20px;
    border-radius: 50%;
    background: var(--icon-blue);
    margin-bottom: 6px;
  }
  .contact-phone { left: 34px; top: 212px; }
  .contact-web { left: 200px; top: 212px; }
  .contact-address { left: 370px; top: 212px; }

  /* Back */
  .back .wordmark { left: 50%; top: 92px; transform: translateX(-50%); font-size: 46px; }
  .back .rule-left { left: 0; width: 140px; top: 125px; }
  .back .rule-right { right: 0; width: 130px; top: 125px; }
  .back-band {
    position: absolute;
    left: 0; right: 0; bottom: 0;
    height: 80px;
    background: var(--band-blue);
    display: flex;
    align-items: center;
    justify-content: center;
    color: #ffffff;
    font-size: 18px;
    letter-spacing: .5px;
  }
</style>
</head>
<body>
  <section class="card front" aria-label="Card front">
    <div class="card-tint" role="img" aria-label="Faint light-blue geometric background"></div>
    <div class="wordmark"><span class="wordmark-dot"></span>Nectra</div>
    <div class="rule"></div>
    <div class="holder">
      <p class="holder-name"><span class="first">FIRST</span> LAST</p>
      <p class="holder-role">Director</p>
    </div>
    <div class="contact contact-phone">
      <svg class="contact-icon" viewBox="0 0 20 20"><circle cx="10" cy="10" r="10" fill="#5b82cf"/><path d="M7 6.5c.4-.4.9-.4 1.2 0l.8 1.1c.2.3.2.7-.1 1l-.5.5c.5 1 1.2 1.7 2.2 2.2l.5-.5c.3-.3.7-.3 1-.1l1.1.8c.4.3.4.8 0 1.2l-.6.6c-.5.5-1.4.6-2.1.2C8.8 12.6 7.4 11.2 6.5 9.6c-.4-.7-.3-1.6.2-2.1z" fill="#fff"/></svg>
      <p>0410 000 000</p>
      <p>(02) 0000 0000</p>
    </div>
    <div class="contact contact-web">
      <svg class="contact-icon" viewBox="0 0 20 20"><circle cx="10" cy="10" r="10" fill="#5b82cf"/><circle cx="10" cy="10" r="5" fill="none" stroke="#fff" stroke-width="1.2"/><path d="M5 10h10M10 5v10M7.5 6c1.5 2.5 1.5 5.5 0 8M12.5 6c-1.5 2.5-1.5 5.5 0 8" fill="none" stroke="#fff" stroke-width="1"/></svg>
      <p>xxx@youremail.com.au</p>
      <p>www.yourwebsite.com.au</p>
    </div>
    <div class="contact contact-address">
      <svg class="contact-icon" viewBox="0 0 20 20"><circle cx="10" cy="10" r="10" fill="#5b82cf"/><path d="M10 4.5a3.5 3.5 0 0 0-3.5 3.5c0 2.6 3.5 6.5 3.5 6.5s3.5-3.9 3.5-6.5A3.5 3.5 0 0 0 10 4.5z" fill="#fff"/><circle cx="10" cy="8" r="1.3" fill="#5b82cf"/></svg>
      <p>123 Human</p>
      <p>Highway, lorewm ABC</p>
      <p>2170</p>
    </div>
  </section>

  <section class="card back" aria-label="Card back">
    <div class="card-tint" role="img" aria-label="Faint light-blue geometric background"></div>
    <div class="rule rule-left"></div>
    <div class="wordmark"><span class="wordmark-dot"></span>Nectra</div>
    <div class="rule rule-right"></div>
    <div class="back-band">www.yourweb.com.au</div>
  </section>
</body>
</html>
```